Website overhaul! mvrcoatings.example

We need some life, professionalism and style put into our site... right now it’s basic and looking unprofessional! Help!

Currently 2 physical store locations that need showcasing and our online store requires easy navigation to categories divided by brand or product type.

80% of our sales are made up of paints for decorating your home, which we sell to the trade painter and end user.

Our company colours are grey and orange - as per our logo so theme based around this with some decent images that stand out.

Target Market(s)

Painter, Decorator, DIY

Industry/Entity Type

Home Improvement

Font styles to use
Sans Serif

Colors
f37122
f78f20

Requirements
Must have
• Clear branding, easy navigation, uncomplicated and clean.

```html
<!DOCTYPE html>
<html lang="en">
<head>
<meta charset="utf-8">
<title>MVR Coatings</title>
<link rel="stylesheet" href="https://fonts.googleapis.com/css2?family=Outfit:wght@400;500;600&family=Montserrat:wght@400;500;600;700&display=swap">
<style>
:root{
  --orange:#f37122;
  --orange-2:#f78f20;
  --peach:#fbd9c2;
  --ink:#333333;
  --muted:#8a8a8a;
  --grey-bg:#f2f2f2;
  --card:#efefef;
  --footer:#3b3b3b;
  --white:#ffffff;
}
*{box-sizing:border-box;margin:0;padding:0}
html,body{width:1200px;height:4357px;overflow:hidden}
body{position:relative;background:var(--white);font-family:"Montserrat",sans-serif;color:var(--ink)}
.abs{position:absolute}
.display{font-family:"Outfit",sans-serif;font-weight:500;color:var(--ink)}
.btn{position:absolute;display:flex;align-items:center;justify-content:center;background:var(--orange);color:var(--white);border-radius:20px;font-family:"Montserrat",sans-serif;font-weight:600}

.topbar{top:0;left:0;width:1200px;height:37px;background:var(--orange);color:var(--white);font-size:11px;display:flex;align-items:center;justify-content:center;gap:8px}
.header{top:37px;left:0;width:1200px;height:98px;background:var(--white)}
.brand{position:absolute;left:184px;top:34px;display:flex;align-items:center;gap:8px;font-family:"Outfit",sans-serif;font-weight:600;font-size:22px;color:var(--orange)}
.brand .dot{width:26px;height:26px;border-radius:50%;background:var(--orange)}
.nav{position:absolute;top:40px;left:449px;display:flex;gap:30px;font-size:13px;font-weight:500;letter-spacing:.2px}
.signup{position:absolute;left:845px;top:40px;font-size:13px;font-weight:600;text-decoration:underline}
.login{left:907px;top:31px;width:109px;height:35px;font-size:13px}

.hero{top:135px;left:0;width:1200px;height:451px;background:linear-gradient(180deg,#8b7a6c 0%,#6e5a4a 45%,#9a8b7e 100%)}
.hero h1{position:absolute;top:142px;width:100%;text-align:center;font-family:"Outfit",sans-serif;font-weight:500;font-size:70px;color:var(--white)}
.hero p{position:absolute;top:247px;width:100%;text-align:center;color:var(--white);font-size:17px;line-height:26px}
.dots{position:absolute;top:400px;left:570px;display:flex;gap:10px;align-items:center}
.dots span{width:8px;height:8px;border-radius:50%;background:var(--white)}
.dots .on{width:20px;height:20px;border:2px solid var(--white);background:transparent;display:flex;align-items:center;justify-content:center}
.dots .on::after{content:"";width:8px;height:8px;border-radius:50%;background:var(--white)}

.section-title{position:absolute;left:0;width:1200px;text-align:center;font-family:"Outfit",sans-serif;font-weight:500;font-size:44px}

.cat{width:405px;height:191px;background:var(--card)}
.cat .icon{position:absolute;left:22px;top:22px;width:48px;height:48px;border-radius:50%;background:var(--peach);display:flex;align-items:center;justify-content:center;z-index:1}
.cat .icon i{width:18px;height:18px;border:2px solid var(--orange);border-radius:3px}
.cat h3{position:absolute;left:22px;top:70px;font-family:"Outfit",sans-serif;font-weight:500;font-size:23px;z-index:1}
.cat p{position:absolute;left:22px;top:104px;font-size:11px;color:var(--muted);z-index:1}
.cat .btn{left:22px;top:135px;width:141px;height:36px;font-size:12px;z-index:1}
.cat .shot{position:absolute;right:18px;top:12px;width:110px;height:167px;border-radius:6px}

.brands-bg{top:1212px;left:0;width:1200px;height:572px;background:var(--grey-bg)}
.tile{width:156px;height:156px;background:var(--white);border:2px solid #e3e3e3;display:flex;align-items:center;justify-content:center;text-align:center;font-family:"Outfit",sans-serif;font-weight:600;font-size:17px;color:var(--ink);padding:0 10px}
.tile.raise{width:188px;height:190px;border:none;box-shadow:0 4px 14px rgba(0,0,0,.08);flex-direction:column;gap:18px;z-index:1}
.tile.raise .pill{border:2px solid var(--orange);color:var(--orange);border-radius:18px;font-family:"Montserrat",sans-serif;font-size:12px;font-weight:600;padding:8px 22px}

.blog{width:263px;height:352px;background:var(--grey-bg)}
.blog .img{position:absolute;left:0;top:0;width:263px;height:186px}
.blog h4{position:absolute;left:22px;top:213px;font-size:15px;font-weight:700;white-space:nowrap}
.blog p{position:absolute;left:22px;top:241px;width:222px;font-size:11.5px;line-height:18.5px;color:var(--muted)}
.blog .more{position:absolute;left:22px;top:303px;font-size:11.5px;font-weight:700;color:var(--orange);display:flex;align-items:center;gap:8px}

.loc-bg{top:2818px;left:0;width:1200px;height:758px;background:var(--grey-bg)}
.loc-card{left:184px;width:391px;height:247px;background:var(--white);border:2px solid #e3e3e3}
.loc-card h3{position:absolute;left:28px;top:30px;font-family:"Outfit",sans-serif;font-weight:500;font-size:23px}
.row{position:absolute;left:28px;display:flex;gap:14px;font-size:12px;color:#666;line-height:20px;align-items:flex-start}
.row svg{flex:none}

.mail{top:3576px;left:0;width:1200px;height:376px;background:linear-gradient(120deg,var(--orange) 0%,var(--orange-2) 50%,var(--orange) 100%)}
.mail h2{position:absolute;top:88px;width:100%;text-align:center;font-family:"Outfit",sans-serif;font-weight:500;font-size:44px;color:var(--white)}
.mail .field{position:absolute;left:305px;top:175px;width:590px;height:49px;background:var(--white);border-radius:25px;padding-left:28px;display:flex;align-items:center;font-size:11px;color:#999}
.mail .btn{left:526px;top:263px;width:149px;height:35px;background:var(--white);color:var(--orange);font-size:12px}

.footer{top:3952px;left:0;width:1200px;height:405px;background:var(--footer);color:var(--white)}
.footer h5{position:absolute;font-family:"Outfit",sans-serif;font-weight:500;font-size:17px}
.footer h5::after{content:"";position:absolute;left:0;top:30px;width:22px;height:2px;background:var(--orange)}
.links{position:absolute;left:391px;top:114px;font-size:11px;line-height:22.5px}
.fc{position:absolute;left:560px;display:flex;gap:14px;font-size:10px;line-height:14px}
.social{position:absolute;top:123px;display:flex;gap:8px}
.social span{width:34px;height:34px;border-radius:50%;background:var(--orange)}
.lang{position:absolute;left:184px;top:201px;width:139px;height:34px;border:1px solid #ccc;font-size:11px;display:flex;align-items:center;justify-content:space-between;padding:0 16px 0 26px}
.rule{position:absolute;left:184px;width:832px;height:1px;background:#555}
.copy{position:absolute;top:335px;width:100%;text-align:center;font-size:11px}
</style>
</head>
<body>

<div class="abs topbar">
  <svg width="13" height="13" viewBox="0 0 14 14"><circle cx="7" cy="7" r="5.8" fill="none" stroke="#fff" stroke-width="1.4"/><path d="M7 3.6V7l2.2 1.4" fill="none" stroke="#fff" stroke-width="1.4"/></svg>
  All stores are OPEN 7.00am-5.00pm Monday to Friday &amp; 8.00am-12.00pm Saturdays / Closed Sundays
</div>

<header class="abs header">
  <div class="brand"><span class="dot"></span>MVR Coatings</div>
  <nav class="nav"><span>HOME</span><span>CONTACT US</span><span>SHOP</span></nav>
  <svg class="abs" style="left:760px;top:37px" width="26" height="24" viewBox="0 0 26 24"><path d="M2 3h4l3 12h12l3-9H8" fill="none" stroke="#333" stroke-width="2"/><circle cx="11" cy="20" r="2" fill="#333"/><circle cx="19" cy="20" r="2" fill="#333"/></svg>
  <svg class="abs" style="left:800px;top:32px" width="34" height="34" viewBox="0 0 34 34"><circle cx="17" cy="17" r="17" fill="#fbd9c2"/><circle cx="15.5" cy="15.5" r="5" fill="none" stroke="#f37122" stroke-width="2"/><path d="M19 19l4 4" stroke="#f37122" stroke-width="2"/></svg>
  <span class="signup">Sign Up</span>
  <span class="btn login">log In</span>
</header>

<section class="abs hero" role="img" aria-label="Living room with a wooden sideboard and wicker chair">
  <h1>Wood Care</h1>
  <p>We sell a range of interior and exterior Wood care products including<br>Nordwood, Granwick and Ambergate</p>
  <div class="dots"><span></span><span class="on"></span><span></span><span></span></div>
</section>

<h2 class="section-title" style="top:650px">Products by Categories</h2>

<div class="abs cat" style="left:184px;top:731px">
  <div class="icon"><i></i></div><h3>Cleaning</h3><p>Free delivery on 3 boxes of PPE or more.</p><span class="btn">Shop Now!</span>
  <div class="shot" role="img" aria-label="Tub of multi-use cleaning wipes" style="width:100px;background:linear-gradient(160deg,#e94a3a,#f5c21b)"></div>
</div>
<div class="abs cat" style="left:611px;top:731px">
  <div class="icon"><i></i></div><h3>Face Masks</h3><p>Free delivery on 3 boxes of PPE or more.</p><span class="btn">Shop Now!</span>
  <div class="shot" role="img" aria-label="Box of disposable face masks" style="width:120px;height:120px;top:12px;background:linear-gradient(160deg,#5aa3d8,#e8f0f6)"></div>
</div>
<div class="abs cat" style="left:184px;top:944px">
  <div class="icon"><i></i></div><h3>Decorating Sundries</h3><p>Free delivery on 3 boxes of face shield or more.</p><span class="btn">Shop Now!</span>
  <div class="shot" role="img" aria-label="Bottle of decorator's varnish" style="width:70px;background:linear-gradient(180deg,#f4f4f4,#cfd8e3)"></div>
</div>
<div class="abs cat" style="left:611px;top:944px">
  <div class="icon"><i></i></div><h3>Paint</h3><p>Free delivery on 3 boxes of face shield or more.</p><span class="btn">Shop Now!</span>
  <div class="shot" role="img" aria-label="Tins of paint and wood filler" style="width:80px;background:linear-gradient(180deg,#7b7b7b,#2e5b3a)"></div>
</div>

<div class="abs brands-bg"></div>
<h2 class="section-title" style="top:1276px">Shop By Brands</h2>
<div class="abs tile" style="left:184px;top:1384px">Kestwick</div>
<div class="abs tile" style="left:354px;top:1384px">Brightmoor</div>
<div class="abs tile" style="left:692px;top:1384px">Oakhaven</div>
<div class="abs tile" style="left:861px;top:1384px">Tansy &amp; Co</div>
<div class="abs tile raise" style="left:506px;top:1368px">Calderton<span class="pill">Shop Now!</span></div>
<div class="abs tile" style="left:184px;top:1554px">Glazeworth</div>
<div class="abs tile" style="left:354px;top:1554px">Bristlecraft</div>
<div class="abs tile" style="left:523px;top:1554px">Whitlock &amp; Reed</div>
<div class="abs tile" style="left:692px;top:1554px">Granwick</div>
<div class="abs tile" style="left:861px;top:1554px">Ambergate</div>

<h2 class="section-title" style="top:1850px">Our Blogs</h2>

<article class="abs blog" style="left:184px;top:1943px"><div class="img" role="img" aria-label="Bright white kitchen" style="background:linear-gradient(180deg,#e8e6e2,#c9c2b8)"></div><h4>Our Guide To Kitchen...</h4><p>From spag bowl sauce splatters to chip pan grease, kitchen walls can be a hotbed for stains and scuffs...</p><span class="more">Read More <svg width="14" height="8" viewBox="0 0 14 8"><path d="M0 4h12M9 1l3 3-3 3" fill="none" stroke="#f37122" stroke-width="1.5"/></svg></span></article>
<article class="abs blog" style="left:469px;top:1943px"><div class="img" role="img" aria-label="Teal pendant lamp against a dark wall" style="background:linear-gradient(180deg,#2f3d44,#1f2a2f)"></div><h4>Whitlock &amp; Reed Launch...</h4><p>We will soon be launching Whitlock and Reed paint on our website shop with special introductory offers..</p><span class="more">Read More <svg width="14" height="8" viewBox="0 0 14 8"><path d="M0 4h12M9 1l3 3-3 3" fill="none" stroke="#f37122" stroke-width="1.5"/></svg></span></article>
<article class="abs blog" style="left:753px;top:1943px"><div class="img" role="img" aria-label="Yellow front door on a white townhouse" style="background:linear-gradient(90deg,#dcdcdc,#e8d54a 50%,#dcdcdc)"></div><h4>Front Door Makeover</h4><p>Everyone seems to be making a statement with their choice of front door colour at the moment...</p><span class="more">Read More <svg width="14" height="8" viewBox="0 0 14 8"><path d="M0 4h12M9 1l3 3-3 3" fill="none" stroke="#f37122" stroke-width="1.5"/></svg></span></article>
<article class="abs blog" style="left:184px;top:2312px"><div class="img" role="img" aria-label="Pink painted building facade" style="background:linear-gradient(160deg,#d93a8a,#b52a6e)"></div><h4>Our Guide To Kitchen...</h4><p>From spag bowl sauce splatters to chip pan grease, kitchen walls can be a hotbed for stains and scuffs...</p><span class="more">Read More <svg width="14" height="8" viewBox="0 0 14 8"><path d="M0 4h12M9 1l3 3-3 3" fill="none" stroke="#f37122" stroke-width="1.5"/></svg></span></article>
<article class="abs blog" style="left:469px;top:2312px"><div class="img" role="img" aria-label="White panelled door with dark handle" style="background:linear-gradient(90deg,#f2f2f2,#dcdcdc)"></div><h4>Whitlock &amp; Reed Launch...</h4><p>We will soon be launching Whitlock and Reed paint on our website shop with special introductory offers..</p><span class="more">Read More <svg width="14" height="8" viewBox="0 0 14 8"><path d="M0 4h12M9 1l3 3-3 3" fill="none" stroke="#f37122" stroke-width="1.5"/></svg></span></article>
<article class="abs blog" style="left:753px;top:2312px"><div class="img" role="img" aria-label="Colourful painted shopfront with hanging sign" style="background:linear-gradient(90deg,#e2452f,#f2c12e 50%,#3a9a6a)"></div><h4>Front Door Makeover</h4><p>Everyone seems to be making a statement with their choice of front door colour at the moment...</p><span class="more">Read More <svg width="14" height="8" viewBox="0 0 14 8"><path d="M0 4h12M9 1l3 3-3 3" fill="none" stroke="#f37122" stroke-width="1.5"/></svg></span></article>

<span class="btn" style="left:525px;top:2705px;width:150px;height:35px;font-size:12px">See All Blogs</span>

<div class="abs loc-bg"></div>
<h2 class="abs display" style="left:184px;top:2882px;font-size:44px">Our Locations</h2>
<p class="abs" style="left:184px;top:2948px;font-size:11.5px;color:#777">CurrentlyWe have two physical store, locations below:</p>

<div class="abs loc-card" style="top:2984px">
  <h3>Ashford Vale</h3>
  <div class="row" style="top:84px"><svg width="22" height="20" viewBox="0 0 22 20"><path d="M2 7c0-3 18-3 18 0v2h-5V7H7v2H2z" fill="#f37122"/><rect x="5" y="10" width="12" height="8" rx="2" fill="#f37122"/><circle cx="11" cy="14" r="2" fill="#fff"/></svg>01632 960417</div>
  <div class="row" style="top:126px"><svg width="22" height="16" viewBox="0 0 22 16"><rect width="22" height="16" fill="#f37122"/><path d="M1 1l10 8 10-8M1 15l7-6M21 15l-7-6" fill="none" stroke="#fff" stroke-width="1.3"/></svg>ASHFORD@MVRCOATINGS.EXAMPLE</div>
  <div class="row" style="top:166px"><svg width="22" height="26" viewBox="0 0 22 26"><path d="M11 1a8 8 0 0 1 8 8c0 6-8 13-8 13S3 15 3 9a8 8 0 0 1 8-8z" fill="#f37122"/><circle cx="11" cy="9" r="3" fill="#fff"/><ellipse cx="11" cy="24" rx="6" ry="1.5" fill="#f37122"/></svg><span>MVR Ashford Vale unit 4 Kestrel Close,<br>Kestrel Road, Ashford Vale, AV3 7QT</span></div>
</div>
<div class="abs loc-card" style="top:3253px">
  <h3>Hartwell</h3>
  <div class="row" style="top:84px"><svg width="22" height="20" viewBox="0 0 22 20"><path d="M2 7c0-3 18-3 18 0v2h-5V7H7v2H2z" fill="#f37122"/><rect x="5" y="10" width="12" height="8" rx="2" fill="#f37122"/><circle cx="11" cy="14" r="2" fill="#fff"/></svg>01632 960582</div>
  <div class="row" style="top:126px"><svg width="22" height="16" viewBox="0 0 22 16"><rect width="22" height="16" fill="#f37122"/><path d="M1 1l10 8 10-8M1 15l7-6M21 15l-7-6" fill="none" stroke="#fff" stroke-width="1.3"/></svg>HARTWELL@MVRCOATINGS.EXAMPLE</div>
  <div class="row" style="top:166px"><svg width="22" height="26" viewBox="0 0 22 26"><path d="M11 1a8 8 0 0 1 8 8c0 6-8 13-8 13S3 15 3 9a8 8 0 0 1 8-8z" fill="#f37122"/><circle cx="11" cy="9" r="3" fill="#fff"/><ellipse cx="11" cy="24" rx="6" ry="1.5" fill="#f37122"/></svg><span>MVR Hartwell 12-14 Mill Yard,<br>Hartwell, HW9 2LX</span></div>
</div>

<div class="abs" role="img" aria-label="Street map showing the store location" style="left:700px;top:2916px;width:278px;height:574px;border-radius:36px;background:linear-gradient(180deg,#eceff1,#dfe6e9)"></div>

<section class="abs mail">
  <h2>Join Our Mailing List</h2>
  <div class="field">Email address</div>
  <span class="btn">Sign Up Now!</span>
</section>

<footer class="abs footer">
  <div class="abs" style="left:205px;top:92px;display:flex;align-items:center;gap:6px;font-family:'Outfit',sans-serif;font-weight:600;font-size:18px;color:var(--orange)"><span style="width:18px;height:18px;border-radius:50%;background:var(--orange)"></span>MVR Coatings</div>
  <div class="lang"><span>English</span><svg width="7" height="5" viewBox="0 0 7 5"><path d="M0 0h7L3.5 5z" fill="#fff"/></svg></div>
  <h5 style="left:391px;top:70px">Quick Links</h5>
  <div class="links">Home<br>Products<br>Brands<br>Shop<br>Contact Us</div>
  <h5 style="left:560px;top:70px">Contact Us</h5>
  <div class="fc" style="top:123px"><svg width="12" height="14" viewBox="0 0 12 14"><path d="M6 0a5 5 0 0 1 5 5c0 4-5 9-5 9S1 9 1 5a5 5 0 0 1 5-5z" fill="#fff"/><circle cx="6" cy="5" r="2" fill="#3b3b3b"/></svg><span>Ashford Vale</span></div>
  <div class="fc" style="top:150px"><svg width="12" height="14" viewBox="0 0 12 14"><rect x="2" y="0" width="8" height="14" rx="1.5" fill="#fff"/><rect x="3.5" y="2" width="5" height="8" fill="#3b3b3b"/></svg><span><b>Call Us</b><br>01632 960417</span></div>
  <div class="fc" style="top:191px"><svg width="12" height="14" viewBox="0 0 12 14"><path d="M6 0a5 5 0 0 1 5 5c0 4-5 9-5 9S1 9 1 5a5 5 0 0 1 5-5z" fill="#fff"/><circle cx="6" cy="5" r="2" fill="#3b3b3b"/></svg><span>Hartwell</span></div>
  <div class="fc" style="top:218px"><svg width="12" height="14" viewBox="0 0 12 14"><rect x="2" y="0" width="8" height="14" rx="1.5" fill="#fff"/><rect x="3.5" y="2" width="5" height="8" fill="#3b3b3b"/></svg><span><b>Call Us</b><br>01632 960582</span></div>
  <h5 style="left:773px;top:75px">Get Social</h5>
  <div class="social" style="left:773px"><span aria-label="Social profile"></span><span aria-label="Social profile"></span><span aria-label="Social profile"></span></div>
  <div class="rule" style="top:313px"></div>
  <p class="copy">Copyright © MVR Coatings 2020. All right Reserved</p>
  <div class="rule" style="top:372px"></div>
</footer>

</body>
</html>
```